Business card design needed

I am a small start up business in the mortgage broking industry based in Sydney called 'keys2nest'. I will be providing residential mortgages to first home owners, investors and people looking to refinance. I would like to see designs that use the colors blue, black, and white - same as my logo (see logo design uploaded)

Target Market(s)

My target market is First Home Owners, property investors, and people looking to refinance. The loans I will be providing are for residential property only at this stage, and my clients will predominantly be in the 30-50yr age bracket.

Industry/Entity Type

Residential

Contact Information for Business Card

Owen Partridge
Director/Mobile Mortgage Broker
keys2nest
PO BOX 4287
Westmead NSW 2145
Mb: 0491 862 307
email: owen@keys2nest.com.au

Requirements
Must have
• please use lower case for business name (i.e. keys2nest)

```html
<!DOCTYPE html>
<html lang="en">
<head>
<meta charset="utf-8">
<title>keys2nest – business card</title>
<link rel="stylesheet" href="https://fonts.googleapis.com/css2?family=Questrial&display=swap">
<style>
  :root {
    --ink: #333333;
    --brand-blue: #1ba7e8;
    --paper: #ffffff;
  }
  html, body {
    margin: 0;
    padding: 0;
    width: 1200px;
    height: 675px;
    overflow: hidden;
    background: var(--paper);
  }
  .card {
    position: relative;
    width: 1200px;
    height: 675px;
    background: var(--paper);
    font-family: "Questrial", sans-serif;
    color: var(--ink);
  }
  .brand {
    position: absolute;
    left: 154px;
    top: 110px;
    display: flex;
    align-items: center;
    gap: 18px;
  }
  .brand-name {
    font-size: 96px;
    line-height: 1;
    letter-spacing: -2.5px;
    color: var(--ink);
  }
  .brand-square {
    width: 26px;
    height: 26px;
    background: var(--brand-blue);
    margin-top: 20px;
  }
  .divider {
    position: absolute;
    left: 693px;
    top: 144px;
    width: 2px;
    height: 123px;
    background: var(--ink);
  }
  .person {
    position: absolute;
    right: 153px;
    top: 226px;
    text-align: right;
  }
  .person-name {
    margin: 0;
    font-size: 48px;
    font-weight: 400;
    line-height: 1;
    letter-spacing: -1px;
    color: var(--ink);
    white-space: nowrap;
  }
  .person-role {
    margin: 6px 0 0;
    font-size: 35px;
    line-height: 1.1;
    color: var(--brand-blue);
  }
  .contact {
    position: absolute;
    right: 153px;
    top: 398px;
    margin: 0;
    text-align: right;
    font-style: normal;
    font-size: 39px;
    line-height: 45.7px;
    color: var(--ink);
    white-space: nowrap;
  }
  .contact span { display: block; }
</style>
</head>
<body>
  <main class="card">
    <div class="brand">
      <span class="brand-name">keys2nest</span>
      <span class="brand-square"></span>
    </div>
    <div class="divider"></div>
    <div class="person">
      <h1 class="person-name">owen partridge</h1>
      <p class="person-role">director</p>
    </div>
    <address class="contact">
      <span>mobile mortgage broker keys2nest</span>
      <span>po box 4287 westmead nsw 2145</span>
      <span>mb: 0491 862 307</span>
      <span>email: owen@keys2nest.com.au</span>
    </address>
  </main>
</body>
</html>
```